Pine Arbor Table & Chair Rentals

We need a business card for a table and chair rental company. We rent tables and chairs for weddings, funerals, business events and parties. We want something that looks clean and elegant while not being too busy. We would like colors in the green and blue hues and avoiding anything orange. We want to make sure the font is large enough to be seen easily.

Target Market(s)

Wedding & Event Rentals

Industry/Entity Type

Events

Contact Information for Business Card

Pine Arbor, sales@pinearborrentals.example, pinearborrentals.example, 555-218-0937

Requirements
Must have
• Easy to read font
Should not have
• Orange anywhere in the design

```html
<!DOCTYPE html>
<html lang="en">
<head>
<meta charset="utf-8">
<title>Pine Arbor Table &amp; Chair Rentals — Business Card</title>
<link rel="stylesheet" href="https://fonts.googleapis.com/css2?family=Montserrat:wght@400;500&family=Open+Sans:wght@400&display=swap">
<style>
  :root {
    --page-bg: #e9ebe6;
    --ink: #141414;
    --paper-light: #f1f2ef;
    --paper-mid: #d6d9d2;
    --foliage: #5f7f25;
    --card-green: #577a0e;
    --card-green-deep: #456309;
    --card-green-soft: #6f8f2a;
    --white: #ffffff;
  }
  * { box-sizing: border-box; margin: 0; padding: 0; }
  html, body { width: 1200px; height: 852px; overflow: hidden; }
  body {
    background: var(--page-bg);
    display: flex;
    flex-direction: column;
    align-items: center;
    justify-content: center;
    gap: 44px;
  }
  .card {
    position: relative;
    width: 630px;
    height: 360px;
    border-radius: 22px;
    overflow: hidden;
    box-shadow: 0 6px 18px rgba(0,0,0,0.18);
  }

  /* Front */
  .card-front .photo {
    position: absolute; inset: 0;
    background:
      radial-gradient(ellipse at 62% 62%, #e7ede0 0 18%, transparent 34%),
      radial-gradient(ellipse at 18% 70%, #dfe4da 0 12%, transparent 26%),
      linear-gradient(200deg, var(--paper-light) 0%, var(--paper-mid) 48%, #8d9a78 78%, var(--foliage) 100%);
  }
  .card-front .brand {
    position: absolute;
    left: 240px; top: 120px;
    transform: rotate(-16deg);
    transform-origin: left top;
    color: var(--ink);
    white-space: nowrap;
  }
  .card-front .brand-name {
    font-family: "Montserrat", sans-serif;
    font-weight: 400;
    font-size: 60px;
    line-height: 1;
  }
  .card-front .tagline {
    font-family: "Montserrat", sans-serif;
    font-weight: 400;
    font-size: 24px;
    margin-top: 12px;
    margin-left: 10px;
  }

  /* Back */
  .card-back {
    background: linear-gradient(160deg, var(--card-green-soft) 0%, var(--card-green) 45%, var(--card-green-deep) 100%);
  }
  .card-back .photo {
    position: absolute; inset: 0;
    background:
      radial-gradient(ellipse at 68% 70%, rgba(150,180,80,0.45) 0 16%, transparent 32%),
      radial-gradient(ellipse at 20% 60%, rgba(140,170,70,0.35) 0 14%, transparent 30%);
  }
  .card-back .brand-name {
    position: absolute;
    left: 54px; bottom: 80px;
    font-family: "Montserrat", sans-serif;
    font-weight: 400;
    font-size: 42px;
    color: var(--white);
    white-space: nowrap;
  }
  .card-back .divider {
    position: absolute;
    left: 318px; top: 140px;
    width: 2px; height: 110px;
    background: var(--white);
  }
  .contact {
    position: absolute;
    left: 338px; top: 122px;
    list-style: none;
    font-family: "Open Sans", sans-serif;
    font-size: 15px;
    color: var(--white);
    white-space: nowrap;
  }
  .contact li {
    display: flex; align-items: center; gap: 9px;
    height: 25px;
  }
  .contact svg { width: 14px; height: 14px; flex: none; fill: var(--white); }
</style>
</head>
<body>

<section class="card card-front">
  <div class="photo" role="img" aria-label="Soft-focus photo of white hydrangea floral balls hanging from white event chairs"></div>
  <div class="brand">
    <div class="brand-name">Pine Arbor</div>
    <div class="tagline">Table and Chair Rentals</div>
  </div>
</section>

<section class="card card-back">
  <div class="photo" role="img" aria-label="Green-tinted blurred photo of floral balls on event chairs"></div>
  <div class="brand-name">Pine Arbor</div>
  <div class="divider"></div>
  <ul class="contact">
    <li>
      <svg viewBox="0 0 16 16" aria-hidden="true"><path d="M2 5c0-2 2-3 6-3s6 1 6 3v1h-3V4.5H5V6H2zM4 7h8l2 6H2z"/></svg>
      555-218-0937
    </li>
    <li>
      <svg viewBox="0 0 16 16" aria-hidden="true"><path d="M1 3h14v10H1zM2.5 4.5 8 9l5.5-4.5v-.2H2.5z" fill-rule="evenodd"/></svg>
      sales@pinearborrentals.example
    </li>
    <li>
      <svg viewBox="0 0 16 16" aria-hidden="true"><circle cx="8" cy="8" r="6.5" fill="none" stroke="#fff" stroke-width="1.3"/><path d="M1.5 8h13M8 1.5c-3 3.5-3 9.5 0 13M8 1.5c3 3.5 3 9.5 0 13" fill="none" stroke="#fff" stroke-width="1.1"/></svg>
      www.pinearborrentals.example
    </li>
  </ul>
</section>

</body>
</html>
```